Custom Manufacturing Job Shop

We are looking for a business card design for Tall Oak Fabrication Inc. Tall Oak is a family owned business that manufactures any custom product to fit a customers needs, whether it is custom 1 piece or production parts, we truly take on projects that others just cant do. to help in your design go to www.talloakfab.example for a more in depth idea. we have the following capabilities that we would like to see on the card somewhere...maybe on the back of a 2 sided card? we are fully open to ideas.
Machining
• Fabrication
• Millwork
• Maintenance
• Laser Cutting
• Precision Forming
Engineering
Blasting/Painting

No matter how big or small, We literally do it all

preferably black or darker cards but we don't mind to see some color if you see a better fit. we are interested in looking at anything that catches attention.
I have attached our logo, if it is needed in a different file type please let me know and I will send it to you if I can. maybe adding some type of drawing or dimensional lines would be something to add?? just throwing ideas out there....

Reason: I added one of our shredder designs and would like to see a few more cards if possible using this. any questions please don't hesitate to ask!!

Target Market(s)

anyone looking for design/manufacturing/machining whether it is custom 1 off parts or production.

Industry/Entity Type

Business

Contact Information for Business Card

preferably darker shades, but also not opposed to some color in the same sense....not too bright

Font styles to use
Serif
Sans Serif

Requirements
Must have
• Dell Marwick
• Direct:555-213-7790
• Cell:555-348-1162
• Fax: 555-907-4425
• 42 Quarry Lane
• Maple Ridge, PA 00000
• I also would request having it in a format I can give to the company making the business cards to edit names/numbers etc. for the entire staff.
Nice to have
• drafting lines? we are open to almost anything....
Should not have
• exotic colors

```html
<!DOCTYPE html>
<html lang="en">
<head>
<meta charset="utf-8">
<title>Tall Oak Fabrication Inc. – Business Card</title>
<link href="https://fonts.googleapis.com/css2?family=Roboto:wght@400;500&display=swap" rel="stylesheet">
<style>
  :root {
    --backdrop: #2b2b2e;
    --card-dark-top: #4a4b58;
    --card-dark-bottom: #2a2b35;
    --band-light: #e9e9eb;
    --card-white: #f7f8f8;
    --ink: #26272c;
    --ink-soft: #55565c;
    --ink-faint: #a9aaae;
    --rule: #8c8d92;
    --logo-light: #eeeef0;
  }
  * { box-sizing: border-box; margin: 0; padding: 0; }
  html, body { width: 1200px; height: 960px; overflow: hidden; }
  body {
    background: var(--backdrop);
    font-family: "Roboto", Arial, sans-serif;
    position: relative;
  }
  .card {
    position: absolute;
    left: 240px;
    width: 720px;
    height: 411px;
    overflow: hidden;
    box-shadow: 0 10px 30px rgba(0,0,0,.45);
  }
  /* Front */
  .card-front { top: 40px; }
  .front-field {
    position: absolute; inset: 0 0 150px 0;
    background: linear-gradient(160deg, var(--card-dark-top), var(--card-dark-bottom));
    display: flex; flex-direction: column; align-items: center; justify-content: center;
  }
  .wordmark {
    display: flex; align-items: center; gap: 16px;
    font-weight: 500; letter-spacing: 4px; text-transform: uppercase;
  }
  .wordmark-square { width: 34px; height: 34px; }
  .front-field .wordmark { color: var(--logo-light); font-size: 62px; }
  .front-field .wordmark-square { background: var(--logo-light); }
  .website {
    margin-top: 10px; font-size: 17px; letter-spacing: 5px; text-transform: uppercase;
  }
  .front-field .website { color: #c9c9ce; }
  .capabilities {
    position: absolute; left: 0; right: 0; bottom: 0; height: 150px;
    background: var(--band-light);
    display: flex; flex-direction: column; justify-content: center; align-items: center;
    color: var(--ink); font-size: 21px; line-height: 1.45;
  }
  /* Back */
  .card-back { top: 510px; background: var(--card-white); padding: 0 40px; }
  .contact-head {
    display: flex; justify-content: space-between; align-items: flex-end;
    padding-top: 48px; padding-bottom: 12px; border-bottom: 1px solid var(--rule);
  }
  .person-name {
    font-size: 27px; font-weight: 400; color: var(--ink);
    letter-spacing: 1px; text-transform: uppercase;
  }
  .address { font-size: 15px; color: var(--ink-soft); }
  .back-logo {
    height: 210px; border-bottom: 1px solid var(--rule);
    display: flex; flex-direction: column; align-items: center; justify-content: center;
  }
  .back-logo .wordmark { color: var(--ink); font-size: 62px; }
  .back-logo .wordmark-square { background: var(--ink); }
  .back-logo .website { color: var(--ink-faint); }
  .phone-row {
    display: flex; justify-content: space-between; align-items: center;
    padding: 18px 6px; border-bottom: 1px solid var(--rule);
    font-size: 17px; color: var(--ink);
  }
  .phone-item { display: flex; align-items: center; gap: 10px; }
  .phone-item svg { width: 18px; height: 18px; fill: var(--ink); }
  .phone-divider { width: 1px; height: 22px; background: var(--ink-faint); }
</style>
</head>
<body>

<section class="card card-front" aria-label="Card front">
  <div class="front-field">
    <div class="wordmark"><span class="wordmark-square"></span>Tall Oak</div>
    <div class="website">talloakfab.example</div>
  </div>
  <div class="capabilities">
    <p>Machining | Fabrication | Millwork | Maintenance</p>
    <p>Laser Cutting | Precision Forming | Engineering | Blasting/Painting</p>
  </div>
</section>

<section class="card card-back" aria-label="Card back">
  <div class="contact-head">
    <h1 class="person-name">Dell Marwick</h1>
    <p class="address">42 Quarry Lane Maple Ridge, PA 00000</p>
  </div>
  <div class="back-logo">
    <div class="wordmark"><span class="wordmark-square"></span>Tall Oak</div>
    <div class="website">talloakfab.example</div>
  </div>
  <div class="phone-row">
    <span class="phone-item">
      <svg viewBox="0 0 24 24" aria-label="Direct"><rect x="1" y="1" width="22" height="22" rx="2"/><path d="M8 5c1 0 2 3 2 4s-1 1-1 2 3 4 4 4 1-1 2-1 4 1 4 2-2 3-3 3C10 19 5 14 5 8c0-1 2-3 3-3z" fill="#f7f8f8"/></svg>
      555-213-7790
    </span>
    <span class="phone-divider"></span>
    <span class="phone-item">
      <svg viewBox="0 0 24 24" aria-label="Cell"><rect x="3" y="1" width="18" height="22" rx="2"/><rect x="6" y="4" width="12" height="13" fill="#f7f8f8"/></svg>
      555-348-1162
    </span>
    <span class="phone-divider"></span>
    <span class="phone-item">
      <svg viewBox="0 0 24 24" aria-label="Fax"><rect x="1" y="1" width="22" height="22" rx="2"/><rect x="5" y="4" width="14" height="6" fill="#f7f8f8"/><rect x="5" y="13" width="3" height="3" fill="#f7f8f8"/><rect x="10" y="13" width="3" height="3" fill="#f7f8f8"/><rect x="15" y="13" width="3" height="3" fill="#f7f8f8"/></svg>
      555-907-4425
    </span>
  </div>
</section>

</body>
</html>
```